PowerPoint Design Project

Have a Power Point we want someone to make really cool! About 10 pages and just need someone to build on what we've done.

Target Market(s)

Technology Mfgs/VARs Sales People and VP of Sales

Industry/Entity Type

Build

```html
<!DOCTYPE html>
<html lang="en">
<head>
<meta charset="utf-8">
<title>Why Offer Financing</title>
<link href="https://fonts.googleapis.com/css2?family=Carlito:wght@400;700&family=Roboto+Condensed:wght@700&display=swap" rel="stylesheet">
<style>
  :root {
    --title-blue: #1b5c9e;
    --subtitle-green: #5a8c1c;
    --body-grey: #4a4a4a;
    --bullet-grey: #555a60;
    --chevron-blue: #2f5fb3;
    --footer-blue: #0d5396;
    --footer-green: #79a32a;
    --divider: #b8bcc0;
    --canvas: #ffffff;
  }
  * { margin: 0; padding: 0; box-sizing: border-box; }
  html, body { width: 1200px; height: 900px; overflow: hidden; }
  body {
    font-family: "Carlito", "Calibri", sans-serif;
    background: var(--canvas);
  }
  .slide {
    position: relative;
    width: 1200px;
    height: 900px;
    overflow: hidden;
    background: linear-gradient(160deg, #f1f2f3 0%, #ffffff 30%, #f7f7f8 55%, #ebecee 100%);
  }
  .backdrop-texture {
    position: absolute; left: 0; top: 0; width: 1200px; height: 806px;
    background: radial-gradient(ellipse at 80% 30%, rgba(255,255,255,0.8), rgba(255,255,255,0) 60%);
  }
  .slide-title {
    position: absolute; left: 57px; top: 40px;
    font-size: 42px; font-weight: 400; color: var(--title-blue);
  }
  .slide-subtitle {
    position: absolute; left: 57px; top: 112px;
    font-size: 31px; font-weight: 700; color: var(--subtitle-green);
  }
  .column-left { position: absolute; left: 58px; top: 218px; width: 510px; }
  .section-heading {
    font-size: 33px; font-weight: 700; color: var(--title-blue);
    line-height: 1.2;
  }
  .section-text {
    font-size: 23px; line-height: 36px; color: var(--body-grey);
    margin-top: 4px;
  }
  .section-text .line { display: block; text-align: justify; text-align-last: justify; }
  .section-text .line:last-child { text-align-last: left; }
  .section + .section { margin-top: 18px; }
  .divider {
    position: absolute; left: 602px; top: 280px; width: 2px; height: 520px;
    background: linear-gradient(to bottom, transparent, var(--divider) 20%, var(--divider) 80%, transparent);
  }
  .column-right { position: absolute; left: 645px; top: 221px; width: 500px; }
  .point-list { list-style: none; margin-top: 6px; }
  .point-list li {
    display: flex; align-items: center; height: 61.5px;
    font-size: 28px; color: var(--bullet-grey);
  }
  .chevron { width: 18px; height: 16px; margin-left: 2px; margin-right: 25px; flex: none; }
  .footer-rule { position: absolute; left: 0; top: 806px; width: 1200px; height: 8px; background: var(--footer-green); }
  .footer {
    position: absolute; left: 0; top: 814px; width: 1200px; height: 86px;
    background: var(--footer-blue);
  }
  .footer-text {
    position: absolute; left: 53px; top: 29px;
    font-family: "Roboto Condensed", "Arial Narrow", sans-serif;
    font-size: 24px; font-weight: 700; color: #ffffff;
  }
  .brand-square {
    position: absolute; right: 0; top: 0; width: 87px; height: 86px;
    background: #ffffff;
  }
  .brand-square::after {
    content: ""; position: absolute; left: 18px; top: 18px; width: 50px; height: 50px;
    background: var(--footer-blue);
  }
</style>
</head>
<body>
<main class="slide">
  <div class="backdrop-texture" role="img" aria-label="Soft abstract light grey background texture"></div>

  <h1 class="slide-title">Why Offer Financing…</h1>
  <h2 class="slide-subtitle">How will this help you make money?</h2>

  <div class="column-left">
    <section class="section">
      <h3 class="section-heading">Heading 1</h3>
      <p class="section-text">
        <span class="line">Lorem ipsum dolor sit ipsum Lorem ipsum</span>
        <span class="line">dolor sit ipsum Lorem ipsum dolor sit ipsum</span>
        <span class="line">Lorem ipsum dolor sit ipsum Lorem ipsum</span>
        <span class="line">dolor sit ipsum Lorem ipsum dolor sit ipsum</span>
        <span class="line">Lorem ipsum dolor sit ipsum Lorem ipsum</span>
        <span class="line">dolor sit ipsum Lorem ipsum</span>
      </p>
    </section>
    <section class="section">
      <h3 class="section-heading">Heading 2</h3>
      <p class="section-text">
        <span class="line">Lorem ipsum dolor sit ipsum Lorem ipsum</span>
        <span class="line">dolor sit ipsum Lorem ipsum dolor sit ipsum</span>
        <span class="line">Lorem ipsum dolor sit ipsum Lorem ipsum</span>
        <span class="line">dolor sit ipsum Lorem ipsum dolor sit ipsum</span>
        <span class="line">Lorem ipsum dolor sit</span>
      </p>
    </section>
  </div>

  <div class="divider"></div>

  <div class="column-right">
    <h3 class="section-heading">Heading 3</h3>
    <ul class="point-list">
      <li><svg class="chevron" viewBox="0 0 18 16"><path d="M2 2l6 6-6 6M9 2l6 6-6 6" fill="none" stroke="var(--chevron-blue)" stroke-width="2.6"/></svg>Lorem ipsum dolor sit ipsum</li>
      <li><svg class="chevron" viewBox="0 0 18 16"><path d="M2 2l6 6-6 6M9 2l6 6-6 6" fill="none" stroke="var(--chevron-blue)" stroke-width="2.6"/></svg>Lorem ipsum dolor sit ipsum</li>
      <li><svg class="chevron" viewBox="0 0 18 16"><path d="M2 2l6 6-6 6M9 2l6 6-6 6" fill="none" stroke="var(--chevron-blue)" stroke-width="2.6"/></svg>Lorem ipsum dolor sit ipsum</li>
      <li><svg class="chevron" viewBox="0 0 18 16"><path d="M2 2l6 6-6 6M9 2l6 6-6 6" fill="none" stroke="var(--chevron-blue)" stroke-width="2.6"/></svg>Lorem ipsum dolor sit ipsum</li>
      <li><svg class="chevron" viewBox="0 0 18 16"><path d="M2 2l6 6-6 6M9 2l6 6-6 6" fill="none" stroke="var(--chevron-blue)" stroke-width="2.6"/></svg>Lorem ipsum dolor sit ipsum</li>
      <li><svg class="chevron" viewBox="0 0 18 16"><path d="M2 2l6 6-6 6M9 2l6 6-6 6" fill="none" stroke="var(--chevron-blue)" stroke-width="2.6"/></svg>Lorem ipsum dolor sit ipsum</li>
      <li><svg class="chevron" viewBox="0 0 18 16"><path d="M2 2l6 6-6 6M9 2l6 6-6 6" fill="none" stroke="var(--chevron-blue)" stroke-width="2.6"/></svg>Lorem ipsum dolor sit ipsum</li>
      <li><svg class="chevron" viewBox="0 0 18 16"><path d="M2 2l6 6-6 6M9 2l6 6-6 6" fill="none" stroke="var(--chevron-blue)" stroke-width="2.6"/></svg>Lorem ipsum dolor sit ipsum</li>
    </ul>
  </div>

  <div class="footer-rule"></div>
  <footer class="footer">
    <p class="footer-text">Copyright@Harbor Lane Capital</p>
    <div class="brand-square" aria-hidden="true"></div>
  </footer>
</main>
</body>
</html>
```